Label designs for three different cider varieties

The Hollin Perry Works is a family run business. We have been making cider within the family as a hobby for over 100 years and we have recently decided to start to try to sell the cider. Therefore this project is to create a logo and three product labels for three different varieties of cider. So we should end up with four files; one for the logo and one for each of the labels. The files need to be in an editable format for us so that we can add edit the batch numbers e.g. PNG file.
For the logo we would like to use the Lark Family Shield since Lark is our family name. We would like it adapted into a cider themed crest, for example with apples and trees. We are open to ideas about the logo but this is just our initial idea. Example of the original Lark Family Shield can be seen in the link below:
http://www.plumevault.net/coats/Lark-England.jpg
The labels should be no bigger than 93mm in height and 213mm in length. Each label should be similar in style so it is clear the three different varieties of cider are from the same company. Each label must have the following information since this is a legal requirement:
- The logo you have created
- The Hollin Perry Works Ltd.
- 42 Milford Terrace, Taunton, Somerset, TA4 9QJ
- Alcohol: 6% vol
- 500ml
- Allergens: Contains Sulphites for freshness
- There needs to be space on the label for batch numbers. This is four numbers e.g. 1701.
- Family craft cider makers using only premium apples from our own traditional Somerset orchard.
The names of the three cider varieties are:
- Hollin Traditional
- Hollin Golden
- Hollin Quarrow
Our initial idea is that each variety would have its own colour associated with it; i.e. black themed label for Hollin Traditional, gold themed label for Hollin Golden and a red themed label for Hollin Quarrow. The crest logo you have created would then be in the themed colour for that cider variety i.e. black, gold or red.
We would like the labels to reflect the following themes for our brand:
- High end premium brand
- Clean and simple design
- Modern
Overall we are very open to ideas and we do not want to constrain your creativity. All of the above is just our initial ideas but we would love to see what ideas you have. The only things that cannot change are what must be on the label since this is a legal requirement we have to meet.

```html
<!DOCTYPE html>
<html lang="en">
<head>
<meta charset="utf-8">
<title>Hollin Perry Works – Cider Labels</title>
<link rel="stylesheet" href="https://fonts.googleapis.com/css2?family=Teko:wght@400;500;600&display=swap">
<style>
  :root {
    --ink: #231f20;
    --paper: #ffffff;
    --golden: #f0ae2a;
    --traditional: #2d5432;
    --quarrow: #9d2f1d;
    --crest-dark: #1f1c1d;
  }
  * { box-sizing: border-box; margin: 0; padding: 0; }
  html, body {
    width: 905px; height: 1200px; overflow: hidden;
    background: var(--paper);
  }
  body { font-family: "Teko", "Arial Narrow", sans-serif; color: var(--ink); position: relative; }

  .label {
    position: absolute; left: 0; width: 905px; height: 390px;
    border: 2px solid var(--ink); background: var(--paper); overflow: hidden;
  }
  .label--golden { top: 0; --theme: var(--golden); }
  .label--traditional { top: 405px; --theme: var(--traditional); }
  .label--quarrow { top: 810px; --theme: var(--quarrow); }

  .label__band {
    position: absolute; left: 0; right: 0; top: 249px; bottom: 0;
    background: var(--theme);
  }
  .label__batch {
    position: absolute; left: 32px; top: 28px; font-size: 15px; font-weight: 500; line-height: 1;
  }
  .label__title {
    position: absolute; left: 0; right: 0; top: 22px; text-align: center;
    font-size: 54px; font-weight: 600; line-height: 1; letter-spacing: 0.5px; text-transform: uppercase;
  }
  .label__story {
    position: absolute; left: 32px; top: 126px; font-size: 16px; font-weight: 500; line-height: 18px;
  }
  .label__address {
    position: absolute; left: 677px; width: 200px; top: 28px; text-align: center;
    font-size: 15px; font-weight: 500; line-height: 17px;
  }
  .label__crest {
    position: absolute; left: 348px; top: 80px; width: 209px; height: 229px;
  }
  .label__company {
    position: absolute; left: 0; right: 0; top: 316px; text-align: center;
    color: var(--paper); font-size: 28px; font-weight: 500; line-height: 1;
  }
  .label__allergens {
    position: absolute; left: 29px; top: 344px; color: var(--paper);
    font-size: 11px; font-weight: 500; line-height: 1;
  }
  .label__volume {
    position: absolute; left: 771px; width: 100px; top: 310px; text-align: center;
    color: var(--paper); font-size: 26px; font-weight: 500; line-height: 24px;
  }
</style>
</head>
<body>

<section class="label label--golden">
  <div class="label__band"></div>
  <p class="label__batch">Batch Number</p>
  <h1 class="label__title">Hollin Golden</h1>
  <p class="label__story">Family craft cider makers,<br>using only premium apples<br>from our own traditional<br>Somerset orchard.</p>
  <p class="label__address">The Hollin Perry Works Ltd.<br>42 Milford Terrace,<br>Taunton,<br>Somerset,<br>TA4 9QJ</p>
  <svg class="label__crest" role="img" aria-label="Family shield crest with apple, leaves and orchard trees" viewBox="0 0 209 229"><rect width="209" height="229" fill="var(--crest-dark)"/></svg>
  <p class="label__company">The Hollin Perry Works Ltd.</p>
  <p class="label__allergens">Contains Sulphites For Freshness</p>
  <p class="label__volume">500ml<br>6% vol</p>
</section>

<section class="label label--traditional">
  <div class="label__band"></div>
  <p class="label__batch">Batch Number</p>
  <h1 class="label__title">Hollin Traditional</h1>
  <p class="label__story">Family craft cider makers,<br>using only premium apples<br>from our own traditional<br>Somerset orchard.</p>
  <p class="label__address">The Hollin Perry Works Ltd.<br>42 Milford Terrace,<br>Taunton,<br>Somerset,<br>TA4 9QJ</p>
  <svg class="label__crest" role="img" aria-label="Family shield crest with apple, leaves and orchard trees" viewBox="0 0 209 229"><rect width="209" height="229" fill="var(--crest-dark)"/></svg>
  <p class="label__company">The Hollin Perry Works Ltd.</p>
  <p class="label__allergens">Contains Sulphites For Freshness</p>
  <p class="label__volume">500ml<br>6% vol</p>
</section>

<section class="label label--quarrow">
  <div class="label__band"></div>
  <p class="label__batch">Batch Number</p>
  <h1 class="label__title">Hollin Quarrow</h1>
  <p class="label__story">Family craft cider makers,<br>using only premium apples<br>from our own traditional<br>Somerset orchard.</p>
  <p class="label__address">The Hollin Perry Works Ltd.<br>42 Milford Terrace,<br>Taunton,<br>Somerset,<br>TA4 9QJ</p>
  <svg class="label__crest" role="img" aria-label="Family shield crest with apple, leaves and orchard trees" viewBox="0 0 209 229"><rect width="209" height="229" fill="var(--crest-dark)"/></svg>
  <p class="label__company">The Hollin Perry Works Ltd.</p>
  <p class="label__allergens">Contains Sulphites For Freshness</p>
  <p class="label__volume">500ml<br>6% vol</p>
</section>

</body>
</html>
```